Halvern Inquiry Partners PLLC
Law Firm Conducting Investigations
Halvern Inquiry Partners PLLC -
Creative Brief
Professional
Dale Morrow
Attorney
21430 SW 3rd Ave, Suite C2-418 Bellevue, WA 98006
dale@halverninquiry-example.com
www.halverninquiry-example.com
I would like the card to be simple, clean and professional. Please use color schemes that match the logo, but don't use too much gold.
The back of the card should be blank.

```html
<!DOCTYPE html>
<html lang="en">
<head>
<meta charset="utf-8">
<title>Halvern Inquiry Partners PLLC – Business Card</title>
<link href="https://fonts.googleapis.com/css2?family=Arimo:wght@400;700&display=swap" rel="stylesheet">
<style>
  :root {
    --paper: #ffffff;
    --edge: #c9c9c9;
    --gold-dark: #8a6a12;
    --gold: #b8901e;
    --gold-light: #e6cf8a;
    --rule: #b5b5b5;
    --divider: #3a3a3a;
    --ink: #3a3a3a;
    --white: #ffffff;
  }
  * { margin: 0; padding: 0; box-sizing: border-box; }
  html, body {
    width: 1200px;
    height: 689px;
    overflow: hidden;
    background: var(--paper);
    font-family: "Arimo", Arial, sans-serif;
  }
  .card {
    position: relative;
    width: 1200px;
    height: 689px;
    background: var(--paper);
    border: 2px solid var(--edge);
  }
  .brand__mark {
    position: absolute;
    left: 82px;
    top: 66px;
    width: 150px;
    height: 150px;
    background: var(--gold);
  }
  .brand__divider {
    position: absolute;
    left: 277px;
    top: 46px;
    width: 3px;
    height: 238px;
    background: linear-gradient(180deg, var(--divider) 0%, var(--divider) 55%, rgba(58,58,58,0) 100%);
  }
  .brand__name {
    position: absolute;
    left: 305px;
    top: 88px;
    color: var(--gold);
    font-weight: 400;
    font-size: 50px;
    line-height: 66px;
    letter-spacing: 2px;
    text-transform: uppercase;
  }
  .band-rule {
    position: absolute;
    left: 0;
    right: 0;
    top: 326px;
    height: 3px;
    background: var(--rule);
  }
  .name-band {
    position: absolute;
    left: 0;
    right: 0;
    top: 336px;
    height: 60px;
    background: linear-gradient(90deg, var(--gold-dark) 0%, var(--gold) 30%, var(--gold-light) 62%, var(--gold) 82%, var(--gold-dark) 100%);
    display: flex;
    align-items: center;
    padding-left: 296px;
    color: var(--white);
    font-size: 34px;
  }
  .name-band__name { font-weight: 700; }
  .name-band__title { font-weight: 400; }
  .contact {
    position: absolute;
    left: 296px;
    top: 488px;
    font-size: 26px;
    line-height: 40px;
    color: var(--ink);
    list-style: none;
  }
  .contact__label {
    color: var(--gold);
    font-weight: 700;
    margin-right: 4px;
  }
  .website {
    position: absolute;
    right: 42px;
    top: 608px;
    font-size: 26px;
    line-height: 40px;
    font-weight: 700;
    color: var(--gold);
  }
</style>
</head>
<body>
  <main class="card">
    <header class="brand">
      <div class="brand__mark"></div>
      <div class="brand__divider"></div>
      <div class="brand__name">Halvern Inquiry<br>Partners</div>
    </header>

    <div class="band-rule"></div>
    <div class="name-band">
      <span class="name-band__name">Dale Morrow</span>&nbsp;|&nbsp;<span class="name-band__title">Attorney</span>
    </div>

    <ul class="contact">
      <li><span class="contact__label">P:</span> 425-555-0182</li>
      <li><span class="contact__label">E:</span> dale@halverninquiry-example.com</li>
      <li><span class="contact__label">A:</span> 21430 SW 3rd Ave,</li>
      <li>Suite C2-418 Bellevue, WA 98006</li>
    </ul>

    <div class="website">www.halverninquiry-example.com</div>
  </main>
</body>
</html>
```